Chatterly Design Project

To create a Chatterly design which matches my new company website:

www.ferntonassociates.com

And to install on Chatterly so that its up and running.

Original brief for website is at: http://jobs.pixelhive.com.au/job.aspx?Id=572104&draft=true

Upload the completed design to Chatterly.

It Company

```html
<!DOCTYPE html>
<html lang="en">
<head>
<meta charset="utf-8">
<title>Tarvik test2 · Chatterly</title>
<link rel="stylesheet" href="https://fonts.googleapis.com/css2?family=Noto+Sans:wght@400;700&family=Oswald:wght@300&family=Crimson+Text:wght@400&display=swap">
<style>
  :root {
    --page-bg: #eceff5;
    --topbar: #6d84b4;
    --topbar-edge: #4e66a0;
    --panel: #ffffff;
    --panel-edge: #c4cde0;
    --link: #3b5998;
    --title: #1c2a47;
    --muted: #7f7f7f;
    --soft: #eff1f6;
    --rail: #cdd3e1;
    --cover-light: #b9c2cf;
    --cover-mid: #4a5d80;
    --cover-dark: #15254a;
  }
  * { box-sizing: border-box; margin: 0; padding: 0; }
  html, body { width: 1200px; height: 639px; overflow: hidden; }
  body {
    position: relative;
    background: var(--page-bg);
    font-family: "Noto Sans", Arial, sans-serif;
    font-size: 10px;
    color: #333;
  }
  .abs { position: absolute; }

  .top-bar { left: 0; top: 0; width: 1200px; height: 24px; background: var(--topbar); border-bottom: 1px solid var(--topbar-edge); }

  .cover {
    left: 215px; top: 27px; width: 763px; height: 283px;
    background: linear-gradient(90deg, var(--cover-light) 0%, var(--cover-mid) 45%, var(--cover-dark) 75%, #1d3570 100%);
  }
  .brand { left: 250px; top: 43px; display: flex; align-items: center; gap: 8px; color: #fff; }
  .brand-mark { width: 26px; height: 26px; border-radius: 50%; background: #fff; }
  .brand-name { font-family: "Crimson Text", Georgia, serif; font-size: 18px; line-height: 1; }
  .brand-sub { font-family: "Crimson Text", Georgia, serif; font-size: 8px; letter-spacing: 2px; margin-top: 1px; }

  .profile-frame {
    left: 235px; top: 300px; width: 154px; height: 69px;
    background: #fff; border: 1px solid var(--panel-edge); padding: 4px; z-index: 2;
  }
  .profile-pic {
    width: 100%; height: 100%;
    background: linear-gradient(180deg, #d6dbe3, #9aa6b8);
    display: flex; align-items: center; justify-content: center;
    font-size: 14px; font-weight: 700; color: #2f6fb8;
  }

  .head-panel {
    left: 215px; top: 310px; width: 763px; height: 166px;
    background: var(--panel); border: 1px solid var(--panel-edge); border-top: 0;
  }
  .page-title { left: 400px; top: 324px; font-size: 17px; font-weight: 700; color: var(--title); }
  .page-likes { left: 401px; top: 347px; font-size: 9px; color: var(--muted); }
  .btn {
    height: 21px; border: 1px solid #999; border-radius: 2px;
    background: linear-gradient(#fafafa, #e7e7e7);
    font-size: 11px; font-weight: 700; color: #333;
    display: flex; align-items: center; justify-content: center; gap: 3px;
  }
  .btn-liked { left: 851px; top: 325px; width: 58px; }
  .btn-gear { left: 918px; top: 325px; width: 39px; }

  .about-tab { left: 216px; top: 378px; width: 294px; height: 66px; background: var(--soft); border-right: 1px solid #dde2ec; }
  .about-icon {
    left: 240px; top: 398px; width: 30px; height: 30px; border-radius: 50%;
    background: #dfe3ee; border: 1px solid #c3cbdc; color: #9aa5be;
    font-family: Georgia, serif; font-weight: 700; font-size: 15px;
    display: flex; align-items: center; justify-content: center;
  }
  .tab-thumb { top: 378px; width: 100px; height: 66px; }
  .thumb-photo { background: linear-gradient(90deg, #c6ccd5, #5e6b80 80%, #1e2a44); }
  .thumb-word {
    background: linear-gradient(180deg, #0a1530, #1b3366);
    color: #fff; font-family: "Oswald", "Arial Narrow", sans-serif; font-weight: 300;
    font-size: 25px; display: flex; align-items: center; justify-content: center;
  }
  .thumb-more { left: 945px; top: 378px; width: 32px; height: 66px; background: var(--soft); }
  .tab-label { top: 451px; font-size: 10px; color: var(--link); }

  .rail { left: 596px; top: 476px; width: 2px; height: 163px; background: var(--rail); }
  .highlights {
    left: 564px; top: 492px; width: 68px; height: 21px;
    background: #f6f7f9; border: 1px solid #ccd3e2; border-radius: 2px;
    color: #9097a8; font-size: 10px; display: flex; align-items: center; justify-content: center; gap: 4px;
  }

  .card { background: var(--panel); border: 1px solid var(--panel-edge); }
  .composer { left: 215px; top: 539px; width: 369px; height: 68px; }
  .composer-tabs { left: 230px; top: 551px; display: flex; font-size: 10px; font-weight: 700; color: var(--link); }
  .composer-tabs span { display: flex; align-items: center; gap: 5px; padding: 0 14px; border-right: 1px solid #e3e6ee; }
  .composer-tabs span:first-child { padding-left: 0; color: #333; }
  .composer-tabs span:last-child { border-right: 0; }
  .tab-icon { width: 12px; height: 11px; border: 1px solid #8a6f2c; background: #f7e4a8; border-radius: 1px; }
  .write-box {
    left: 221px; top: 575px; width: 358px; height: 26px;
    border: 1px solid #bdc7d8; background: #fff; padding: 5px; font-size: 11px; color: #777;
  }
  .friends { left: 610px; top: 539px; width: 369px; height: 110px; }
  .friends-count { left: 624px; top: 551px; font-size: 22px; font-weight: 700; color: var(--link); }
  .friends-title { left: 645px; top: 554px; font-size: 10px; font-weight: 700; color: var(--link); }
  .friends-sub { left: 645px; top: 567px; font-size: 9px; color: var(--muted); }
  .friends-rule { left: 624px; top: 587px; width: 341px; height: 1px; background: #e5e8ef; }
  .friend-row { left: 625px; top: 591px; display: flex; gap: 1px; }
  .friend-row span { width: 33px; height: 33px; }

  .create-page {
    left: 991px; top: 36px; width: 75px; height: 19px;
    background: #5b74a8; border: 1px solid #29447e; border-radius: 2px;
    color: #fff; font-size: 10px; font-weight: 700; display: flex; align-items: center; justify-content: center;
  }
  .side-rule { left: 990px; height: 1px; background: #d3d8e4; width: 210px; }
  .year-nav { left: 991px; top: 74px; border-left: 3px solid #d3d8e4; }
  .year-nav li { list-style: none; font-size: 10px; color: #8f9bb5; padding: 4px 0 5px 7px; margin-left: -3px; border-left: 3px solid transparent; }
  .year-nav li.current { border-left-color: var(--link); color: var(--link); font-weight: 700; }
  .ad-head { left: 990px; top: 488px; font-size: 10px; font-weight: 700; color: #666; }
  .ad-name { left: 990px; top: 508px; font-size: 10px; font-weight: 700; color: var(--link); }
  .ad-image {
    left: 990px; top: 525px; width: 90px; height: 67px;
    background: linear-gradient(180deg, #c8d8e6, #a7bccf);
    display: flex; align-items: center; justify-content: center;
    font-size: 11px; font-weight: 700; color: #1f4a2e;
  }
  .ad-like { left: 990px; top: 597px; font-size: 9px; color: #666; }
  .ad-like b { color: var(--link); font-weight: 400; }
  .advertise {
    left: 991px; top: 615px; width: 115px; height: 20px;
    border: 1px solid #999; background: linear-gradient(#fff, #eee);
    font-size: 10px; font-weight: 700; color: #333; display: flex; align-items: center; justify-content: center;
  }
</style>
</head>
<body>
  <header class="abs top-bar"></header>

  <div class="abs cover" role="img" aria-label="Cover photo: businessman's open hand holding a glowing globe against a starry blue sky"></div>
  <div class="abs brand">
    <span class="brand-mark"></span>
    <div>
      <div class="brand-name">Fernton Associates</div>
      <div class="brand-sub">Business Advisors</div>
    </div>
  </div>

  <section class="abs head-panel"></section>
  <div class="abs profile-frame"><div class="profile-pic">Fernton</div></div>

  <h1 class="abs page-title">Tarvik test2</h1>
  <div class="abs page-likes">13 likes</div>
  <div class="abs btn btn-liked">
    <svg width="8" height="8" viewBox="0 0 8 8"><path d="M1 4.2 3 6.2 7 1.6" fill="none" stroke="#555" stroke-width="1.5"/></svg>Liked
  </div>
  <div class="abs btn btn-gear">
    <svg width="9" height="9" viewBox="0 0 10 10"><circle cx="5" cy="5" r="3.2" fill="none" stroke="#555" stroke-width="2" stroke-dasharray="1.6 1"/></svg>
    <svg width="8" height="5" viewBox="0 0 8 5"><path d="M0 0h8L4 5z" fill="#5b74a8"/></svg>
  </div>

  <div class="abs about-tab"></div>
  <div class="abs about-icon">i</div>
  <div class="abs tab-label" style="left:254px">About</div>

  <div class="abs tab-thumb thumb-photo" style="left:517px" role="img" aria-label="Photo album thumbnail"></div>
  <div class="abs tab-thumb thumb-word" style="left:623px">about</div>
  <div class="abs tab-thumb thumb-word" style="left:731px">website</div>
  <div class="abs tab-thumb thumb-word" style="left:837px">blog</div>
  <div class="abs thumb-more"></div>
  <div class="abs tab-label" style="left:516px">Photos</div>
  <div class="abs tab-label" style="left:623px">Photos</div>
  <div class="abs tab-label" style="left:731px">About Me</div>
  <div class="abs tab-label" style="left:837px">Brightcode</div>

  <div class="abs rail"></div>
  <div class="abs highlights">Highlights
    <svg width="7" height="4" viewBox="0 0 8 5"><path d="M0 0h8L4 5z" fill="#9097a8"/></svg>
  </div>

  <div class="abs card composer"></div>
  <div class="abs composer-tabs">
    <span><i class="tab-icon"></i>Status</span>
    <span><i class="tab-icon"></i>Photo / Video</span>
    <span><i class="tab-icon" style="background:#fff;border-color:#b33"></i>Event, Milestone +</span>
  </div>
  <div class="abs write-box">Write something...</div>

  <div class="abs card friends"></div>
  <div class="abs friends-count">6</div>
  <div class="abs friends-title">Friends</div>
  <div class="abs friends-sub">Like Tarvik test2</div>
  <div class="abs friends-rule"></div>
  <div class="abs friend-row" role="img" aria-label="Six friend profile photos">
    <span style="background:#4b5a6a"></span>
    <span style="background:#3d4a3a"></span>
    <span style="background:#8a7466"></span>
    <span style="background:#6c8aa0"></span>
    <span style="background:#b8c8d8"></span>
    <span style="background:#9a6a52"></span>
  </div>

  <aside>
    <div class="abs create-page">Create Page</div>
    <div class="abs side-rule" style="top:65px"></div>
    <ul class="abs year-nav">
      <li class="current">Now</li>
      <li>October</li>
      <li>Born</li>
    </ul>
    <div class="abs ad-head">See Your Ad Here</div>
    <div class="abs side-rule" style="top:504px"></div>
    <div class="abs ad-name">Tarvik test2</div>
    <div class="abs ad-image">Stallworth</div>
    <div class="abs ad-like"><b>Like</b> · Daniel Moray likes this.</div>
    <div class="abs advertise">Advertise Your Page</div>
  </aside>
</body>
</html>
```